Redesign of business card for Birchline Mechanical

We are looking for a new design for our business cards for Birchline Mechanical. We are a plumbing & HVAC construction company, operating on the West Coast of Canada and USA. Logo attached.
Industry/Entity Type
Construction - Plumbing & HVAC
Contact Information for Business Card
Name, address, phone numbers, email, website address
Look and feel
Each slider illustrates characteristics of the customer's brand and the style your logo design should communicate.

```html
<!DOCTYPE html>
<html lang="en">
<head>
<meta charset="utf-8">
<title>Birchline Mechanical – Business Card</title>
<link rel="stylesheet" href="https://fonts.googleapis.com/css2?family=Montserrat:wght@400;500;600;700&display=swap">
<style>
  :root {
    --page-bg: #ebe6df;
    --card-bg: #dcd8d2;
    --ink: #1a1a1a;
    --ink-soft: #3a3a3a;
    --band-dark: #0d0d0d;
    --swoosh: #8a857e;
    --swoosh-light: #c9c3ba;
    --brand-tone: #e6dccd;
  }
  html, body {
    margin: 0;
    padding: 0;
    width: 1200px;
    height: 1047px;
    overflow: hidden;
    background: var(--page-bg);
    font-family: "Montserrat", sans-serif;
  }
  .business-card {
    position: absolute;
    left: 100px;
    top: 251px;
    width: 1000px;
    height: 545px;
    border-radius: 26px;
    background: var(--card-bg);
    overflow: hidden;
    box-shadow: 0 12px 40px rgba(0,0,0,0.12);
  }
  .card-waves {
    position: absolute;
    inset: 0;
    width: 100%;
    height: 100%;
  }
  .brand {
    position: absolute;
    right: 34px;
    top: 150px;
    display: flex;
    align-items: center;
    gap: 14px;
    color: var(--brand-tone);
    font-weight: 600;
    font-size: 30px;
    letter-spacing: 0.5px;
  }
  .brand-square {
    width: 26px;
    height: 26px;
    background: var(--brand-tone);
  }
  .person {
    position: absolute;
    left: 0;
    top: 265px;
    padding-left: 44px;
  }
  .person-bar {
    position: absolute;
    left: 0;
    top: 4px;
    width: 20px;
    height: 64px;
    background: var(--ink);
  }
  .person-name {
    margin: 0;
    font-weight: 700;
    font-size: 37px;
    letter-spacing: 0.8px;
    color: var(--ink);
    line-height: 1.1;
  }
  .person-role {
    margin: 6px 0 0;
    font-weight: 400;
    font-size: 25px;
    color: var(--ink-soft);
  }
  .contact-list {
    position: absolute;
    left: 40px;
    top: 405px;
    margin: 0;
    padding: 0;
    list-style: none;
  }
  .contact-item {
    display: flex;
    align-items: center;
    gap: 8px;
    font-size: 25px;
    color: var(--ink);
    height: 39px;
  }
  .contact-icon {
    width: 22px;
    height: 22px;
    fill: var(--ink);
  }
  .address {
    position: absolute;
    right: 30px;
    top: 440px;
    margin: 0;
    text-align: right;
    font-style: normal;
    font-size: 25px;
    line-height: 39px;
    color: var(--ink);
  }
</style>
</head>
<body>
  <section class="business-card">
    <svg class="card-waves" viewBox="0 0 880 478" preserveAspectRatio="none" aria-hidden="true">
      <path fill="var(--band-dark)" d="M0 0 H880 V205 C830 290 720 300 610 268 C470 228 330 100 0 78 Z"/>
      <path fill="var(--swoosh)" d="M0 84 C330 108 470 240 620 282 C740 314 840 285 880 205 V250 C835 318 720 338 600 305 C460 268 320 132 0 108 Z"/>
      <path fill="none" stroke="var(--swoosh-light)" stroke-width="2" d="M0 86 C330 110 470 230 600 262"/>
    </svg>

    <div class="brand">
      <span class="brand-square"></span>
      <span class="brand-name">Birchline Mechanical</span>
    </div>

    <div class="person">
      <span class="person-bar"></span>
      <h1 class="person-name">DANIEL MERCER</h1>
      <p class="person-role">Managing Director</p>
    </div>

    <ul class="contact-list">
      <li class="contact-item">
        <svg class="contact-icon" viewBox="0 0 24 24"><path d="M6.6 10.8a15 15 0 0 0 6.6 6.6l2.2-2.2a1 1 0 0 1 1-.25 11.4 11.4 0 0 0 3.6.57 1 1 0 0 1 1 1V20a1 1 0 0 1-1 1A17 17 0 0 1 3 4a1 1 0 0 1 1-1h3.5a1 1 0 0 1 1 1c0 1.25.2 2.45.57 3.57a1 1 0 0 1-.25 1z"/></svg>
        <span>123 456 789</span>
      </li>
      <li class="contact-item">
        <svg class="contact-icon" viewBox="0 0 24 24"><path d="M3 5h18a1 1 0 0 1 1 1v12a1 1 0 0 1-1 1H3a1 1 0 0 1-1-1V6a1 1 0 0 1 1-1zm1 2.2V17h16V7.2l-8 5.3z M5 7l7 4.6L19 7z"/></svg>
        <span>info@birchlinemech.com</span>
      </li>
      <li class="contact-item">
        <svg class="contact-icon" viewBox="0 0 24 24"><path d="M12 2a10 10 0 1 0 0 20 10 10 0 0 0 0-20zm-1 17.9A8 8 0 0 1 4.1 11H7c.1 3 1.4 6.3 4 8.9zM4.1 9A8 8 0 0 1 11 4.1C8.9 6.3 7.5 8 7.2 9zm8.9 10.9c2.6-2.6 3.9-5.9 4-8.9h2.9a8 8 0 0 1-6.9 8.9zM16.8 9C16.5 8 15.1 6.3 13 4.1A8 8 0 0 1 19.9 9z"/></svg>
        <span>www.birchlinemech.com</span>
      </li>
    </ul>

    <address class="address">
      Your address, City<br>
      State, Zip 1234
    </address>
  </section>
</body>
</html>
```